High End Business Card Design for Flooring Store

Looking for a new card design for our hardwood flooring company. We have no print budget for these and are open to cards made from wood, metal, cardstock with embossed print ... or any combination of these. No plastic.

We sell luxury products and I want the cards to reflect our image of quality and class.

Our contact information as such;
Employee Name
418 Colbrook Blvd.
Marden, ON
K9R-3M5
(555) 214-3968
Employee email @velkaflooring.com

Target Market(s)

Home Builders

Contact Information for Business Card

Emnployee name, business contact information

```html
<!DOCTYPE html>
<html lang="en">
<head>
<meta charset="utf-8">
<title>Velka Flooring – Business Card</title>
<link href="https://fonts.googleapis.com/css2?family=Ubuntu:wght@400&display=swap" rel="stylesheet">
<style>
  :root {
    --backdrop: #cbcbcb;
    --card-black: #1f1f1f;
    --accent-gold: #e8b425;
    --brand-red: #9b2a25;
    --tagline-grey: #6b6b6b;
    --ink: #1b1b1b;
  }
  html, body {
    margin: 0;
    padding: 0;
    width: 1200px;
    height: 1200px;
    overflow: hidden;
    background: var(--backdrop);
  }
  .card {
    position: absolute;
    left: 170px;
    width: 864px;
    height: 505px;
    background: var(--card-black);
    box-shadow: 4px 6px 10px rgba(0,0,0,0.25);
    overflow: hidden;
  }
  .card--front { top: 75px; }
  .card--back { top: 619px; }

  .accent-panel {
    position: absolute;
    inset: 0;
    width: 100%;
    height: 100%;
  }
  .accent-panel polygon { fill: var(--accent-gold); }

  .brand-name {
    position: absolute;
    margin: 0;
    font-family: "Ubuntu", sans-serif;
    font-weight: 400;
    color: var(--brand-red);
    line-height: 1;
    text-align: center;
  }
  .tagline {
    position: absolute;
    margin: 0;
    font-family: "Ubuntu", sans-serif;
    font-weight: 400;
    color: var(--tagline-grey);
    text-align: center;
    line-height: 1.15;
  }

  /* front card */
  .card--front .brand-name { left: 51px; width: 400px; top: 148px; font-size: 72px; }
  .card--front .tagline { left: 51px; width: 400px; top: 228px; font-size: 20px; }

  .employee-name {
    position: absolute;
    right: 68px;
    top: 100px;
    margin: 0;
    font-family: "Ubuntu", sans-serif;
    font-weight: 400;
    font-size: 35px;
    color: var(--ink);
  }
  .contact-list {
    position: absolute;
    right: 60px;
    top: 238px;
    margin: 0;
    padding: 0;
    list-style: none;
    font-family: "Ubuntu", sans-serif;
    font-size: 21px;
    color: var(--ink);
    text-align: right;
  }
  .contact-list li {
    display: flex;
    justify-content: flex-end;
    align-items: flex-start;
    gap: 20px;
    line-height: 33px;
  }
  .contact-list .contact-address { margin-top: 22px; line-height: 32.5px; }
  .contact-icon { width: 18px; height: 33px; flex: none; }
  .contact-icon svg { width: 18px; height: 18px; margin-top: 8px; fill: var(--ink); }

  /* back card */
  .card--back .brand-name { left: 0; width: 864px; top: 165px; font-size: 118px; }
  .card--back .tagline { left: 0; width: 864px; top: 282px; font-size: 32px; }
</style>
</head>
<body>

<section class="card card--front" aria-label="Business card front">
  <svg class="accent-panel" viewBox="0 0 691 404" preserveAspectRatio="none" aria-hidden="true">
    <polygon points="381,0 442,0 485,40 520,0 647,0 691,40 691,404 454,404 295,260 387,155 307,82"/>
  </svg>

  <p class="brand-name">Velka</p>
  <p class="tagline">Bois Franc &amp; Finition<br>Hardwood &amp; Finishing</p>

  <h1 class="employee-name">Employee Name</h1>
  <ul class="contact-list">
    <li><span>(555) 214-3968</span>
      <span class="contact-icon"><svg viewBox="0 0 24 24"><path d="M7 1h10a2 2 0 0 1 2 2v18a2 2 0 0 1-2 2H7a2 2 0 0 1-2-2V3a2 2 0 0 1 2-2zm0 3v14h10V4H7zm5 15.5a1 1 0 1 0 0 2 1 1 0 0 0 0-2z"/></svg></span></li>
    <li><span>email @velkaflooring.com</span>
      <span class="contact-icon"><svg viewBox="0 0 24 24"><path d="M3 5h18a1 1 0 0 1 1 1v12a1 1 0 0 1-1 1H3a1 1 0 0 1-1-1V6a1 1 0 0 1 1-1zm9 7.5L20 7.5V7H4v.5z"/></svg></span></li>
    <li class="contact-address"><span>418 Colbrook Blvd.<br>Marden, ON<br>K9R-3M5</span>
      <span class="contact-icon"><svg viewBox="0 0 24 24"><path d="M12 2a7 7 0 0 1 7 7c0 5-7 13-7 13S5 14 5 9a7 7 0 0 1 7-7zm0 4.5a2.5 2.5 0 1 0 0 5 2.5 2.5 0 0 0 0-5z"/></svg></span></li>
  </ul>
</section>

<section class="card card--back" aria-label="Business card back">
  <p class="brand-name">Velka</p>
  <p class="tagline">Bois Franc &amp; Finition<br>Hardwood &amp; Finishing</p>
</section>

</body>
</html>
```